A small boutique Accounting and Mortgage Broking firm needs a business card design

Torvel is a Brisbane based boutique accounting and mortgage broking firm. We offer a range of extensive financial services like accounting, tax consulting, book-keeping and mortgage broking.
We need a business card that stands out. The content can stay as it is on the existing card unless you recommend us to change anything on it for a better design.
Please remove the mobile number and give us a suitable format to change the details like email address and name.
Contact Information for Business Card
Dilan Karodi
Torvel Group Pty Ltd
3/412 Wendle Rd Kelmore QLD 4120
PO Box 829 Kelmore QLD 4120
T 07 3184 5526
F 07 3952 1873
E dkarodi@torvel-example.net.au
Accountants Tax Agents, Mortgage Brokers
www.torvel-example.net.au

```html
<!DOCTYPE html>
<html lang="en">
<head>
<meta charset="utf-8">
<title>Torvel business card</title>
<link rel="stylesheet" href="https://fonts.googleapis.com/css2?family=Lato:wght@300;400;900&family=Cinzel:wght@400;700&display=swap">
<style>
  :root {
    --bg: #e9e6e1;
    --card-light: #fbfbfb;
    --card-light-edge: #e6e6e6;
    --card-dark: #3a3b3d;
    --card-dark-deep: #262729;
    --green: #7dbb2e;
    --grey-text: #5d5f62;
    --ink: #2e2f31;
    --rule: #6b6d70;
    --white: #ffffff;
  }
  * { box-sizing: border-box; margin: 0; padding: 0; }
  html, body { width: 1200px; height: 1023px; overflow: hidden; }
  body { background: var(--bg); font-family: "Lato", sans-serif; position: relative; }

  .card {
    position: absolute;
    width: 540px;
    height: 310px;
    border-radius: 18px;
    box-shadow: 0 14px 30px rgba(0,0,0,0.18);
  }

  /* Front */
  .card--front {
    left: 70px; top: 150px;
    background: linear-gradient(160deg, var(--white), var(--card-light) 60%, var(--card-light-edge));
    color: var(--grey-text);
  }
  .brand { position: absolute; display: flex; align-items: center; gap: 12px; }
  .brand__dot { width: 40px; height: 40px; border-radius: 50%; background: var(--grey-text); }
  .brand__name { font-weight: 900; font-size: 44px; line-height: 1; letter-spacing: -1px; color: var(--green); }
  .card--front .brand { left: 36px; top: 34px; }
  .tagline { position: absolute; font-weight: 300; font-size: 17px; letter-spacing: 0.5px; text-transform: uppercase; }
  .card--front .tagline { left: 36px; top: 88px; color: var(--grey-text); }
  .holder-name {
    position: absolute; left: 36px; top: 122px;
    font-family: "Cinzel", serif; font-weight: 700; font-size: 20px; color: var(--green);
    font-variant: small-caps;
  }
  .divider { position: absolute; left: 36px; right: 30px; top: 160px; height: 1.5px; background: var(--rule); }
  .contact-list { position: absolute; left: 36px; top: 176px; list-style: none; font-size: 13px; color: var(--ink); }
  .contact-list li { display: flex; align-items: center; gap: 10px; height: 22px; }
  .contact-list svg { width: 13px; height: 13px; fill: var(--green); flex: none; }
  .address {
    position: absolute; right: 30px; top: 176px; text-align: right;
    font-style: normal; font-size: 14px; line-height: 22px; color: var(--ink);
  }

  /* Back */
  .card--back {
    left: 590px; top: 520px;
    background: linear-gradient(150deg, #4a4b4e, var(--card-dark) 45%, var(--card-dark-deep));
    color: var(--white);
  }
  .card--back .brand { left: 50%; top: 78px; transform: translateX(-50%); }
  .card--back .brand__dot { width: 56px; height: 56px; background: var(--white); }
  .card--back .brand__name { font-size: 62px; color: var(--white); }
  .card--back .tagline { left: 0; right: 0; top: 158px; text-align: center; font-size: 22px; letter-spacing: 1px; }
  .services {
    position: absolute; left: 0; right: 0; bottom: 34px; text-align: center;
    font-family: "Cinzel", serif; font-size: 13px; letter-spacing: 0.8px;
  }
</style>
</head>
<body>

<section class="card card--front">
  <div class="brand">
    <span class="brand__dot"></span>
    <span class="brand__name">Torvel</span>
  </div>
  <p class="tagline">Care. Clarity. Progress.</p>
  <h1 class="holder-name">Dilan Karodi</h1>
  <div class="divider"></div>
  <ul class="contact-list">
    <li><svg viewBox="0 0 16 16"><path d="M3 1h3l1.5 4-2 1.3a9 9 0 0 0 4.2 4.2L11 8.5l4 1.5v3a2 2 0 0 1-2 2A12 12 0 0 1 1 3a2 2 0 0 1 2-2z"/></svg>07 3184 5526</li>
    <li><svg viewBox="0 0 16 16"><path d="M4 1h7v4H4zM1 6h14v7h-3v2H4v-2H1zM5 10v4h6v-4z"/></svg>07 3952 1873</li>
    <li><svg viewBox="0 0 16 16"><path d="M1 3h14v10H1zM2 4l6 5 6-5v1L8 10 2 5z"/></svg>dkarodi@torvel-example.net.au</li>
    <li><svg viewBox="0 0 16 16"><path d="M8 1a7 7 0 1 0 0 14A7 7 0 0 0 8 1zm0 1.5c1 1 1.6 2.6 1.8 4.5H6.2C6.4 5.1 7 3.5 8 2.5zM2.6 7h2.2c.1-1.6.5-3 1.1-4A5.6 5.6 0 0 0 2.6 7zm8.6 0h2.2a5.6 5.6 0 0 0-3.3-4c.6 1 1 2.4 1.1 4zM2.6 9a5.6 5.6 0 0 0 3.3 4c-.6-1-1-2.4-1.1-4zm3.6 0c.2 1.9.8 3.5 1.8 4.5 1-1 1.6-2.6 1.8-4.5zm5 0c-.1 1.6-.5 3-1.1 4a5.6 5.6 0 0 0 3.3-4z"/></svg>www.torvel-example.net.au</li>
  </ul>
  <address class="address">
    3/412 Wendle Rd<br>
    Kelmore QLD 4120<br>
    PO Box 829 Kelmore QLD 4120
  </address>
</section>

<section class="card card--back">
  <div class="brand">
    <span class="brand__dot"></span>
    <span class="brand__name">Torvel</span>
  </div>
  <p class="tagline">Care. Clarity. Progress.</p>
  <p class="services">Accountants - Tax Agents - Mortgage Brokers</p>
</section>

</body>
</html>
```